Doctors Office Web Design

Name of the business is Lin-Yue Hart M.D.
We need a web design that is attractive for women that want to see Dr. Lin-Yue Hart for Obstetrician Gynecology and Pregnancy care. Dr. Hart earned her degree from Carrow Ridge Medical College of obstetrician gynecology. We want to attract women of child bearing ages to come to our offices for health, education, and pregnancies.

Please visit http://www.drhartclinicweb.com/ to help you get a feel for who we are. We will be adding some pictures and logo in the next few days.

We are looking for to have pages for and tabs including
About Us- History, Our Staff, Dr. Hart
Patient Information- Appointments, E-Prescriptions, Payments Accepted, Insurance
Health- General, Sexual, Mental, Affiliates
Pregnancy- Minimally invasive surgery(our specialty), 4-D Ultra Sound, Hospital Affiliations
Media- News,Pictures, Videos
Locations- Palmer Office, Westvale Office

The colors we would like to use are pastel colors, magenta, and plum

Target Market(s)

Women of all ages with an emphasis on 25-65 year olds

Industry/Entity Type

Business

Requirements
Must have
• Needs to include a location for a our videos and pictures that I will submit shortly. We also want a map to our location or atleast a place for one.
Nice to have
• A place for a google map of our office locations.

```html
<!DOCTYPE html>
<html lang="en">
<head>
<meta charset="utf-8">
<title>Dr. Hart – Obstetrics &amp; Gynecology</title>
<link rel="stylesheet" href="https://fonts.googleapis.com/css2?family=Quicksand:wght@400;500;700&family=Arimo:wght@400;700&family=Parisienne&display=swap">
<style>
:root{
  --magenta:#cc5aa0;
  --magenta-dark:#b23f86;
  --plum:#452037;
  --plum-text:#7a1f55;
  --wine:#9a0f4e;
  --sky:#b9ccd9;
  --sky-deep:#9ab5c8;
  --mist:#eaeff3;
  --footer:#d3c3cc;
  --footer-text:#7d6a75;
  --footer-head:#6a4c5e;
  --grey-text:#666a70;
  --white:#ffffff;
}
*{box-sizing:border-box;margin:0;padding:0}
html,body{width:1040px;height:1200px;overflow:hidden}
body{position:relative;background:var(--mist);font-family:"Arimo",Arial,sans-serif;color:#333}
.abs{position:absolute}

/* header */
.hero{left:0;top:0;width:1040px;height:466px;background:var(--sky)}
.navbar{left:0;top:12px;width:1040px;height:52px;background:linear-gradient(#d66aad,#b84c8f)}
.nav{left:334px;top:12px;width:706px;height:52px;border-radius:22px 0 0 0;background:linear-gradient(#d66aad,#b84c8f);display:flex;align-items:center;list-style:none;padding-left:8px}
.nav li{font-family:"Quicksand",sans-serif;font-weight:700;font-size:14px;color:var(--white);margin-right:26px;letter-spacing:.1px}
.nav li.active{background:var(--sky-deep);border-radius:14px;padding:6px 8px;margin-right:24px}
.brand{left:124px;top:12px;width:210px;height:103px;background:var(--white);border-radius:0 0 18px 18px;padding:18px 14px 0}
.brand-name{font-family:"Quicksand",sans-serif;font-weight:500;font-size:44px;line-height:44px;color:var(--magenta)}
.brand-tag{font-family:"Quicksand",sans-serif;font-weight:500;font-size:10.5px;color:#2f5a86;margin-top:6px;letter-spacing:.2px}
.portrait{left:138px;top:134px;width:313px;height:317px;border-radius:140px 140px 0 0;background:radial-gradient(ellipse at 50% 40%,#d8c8bc 0%,#c9d5de 60%,rgba(185,204,217,0) 100%)}
.silhouette{left:643px;top:64px;width:275px;height:402px;border-radius:140px 120px 0 0;background:linear-gradient(#c3a7c3,#b597b8);opacity:.6}
.call{right:137px;top:80px;text-align:right;color:var(--white);font-family:"Quicksand",sans-serif}
.call small{display:block;font-size:14px}
.call strong{display:block;font-size:22px;font-weight:500}
.hero-title{right:134px;top:200px;text-align:right;font-family:"Quicksand",sans-serif;color:#8d2d68}
.hero-title b{display:block;font-size:46px;font-weight:700;line-height:50px}
.hero-title span{display:block;font-size:30px;font-weight:500;line-height:32px}
.hero-lead{left:500px;top:284px;width:410px;font-family:"Quicksand",sans-serif;font-weight:700;font-size:13.5px;line-height:17px;color:var(--white)}
.btn-learn{left:728px;top:356px;width:165px;height:38px;border-radius:19px;background:linear-gradient(#fff,#e8e8ec);border:1px solid #ccc;font-family:"Quicksand",sans-serif;font-weight:700;font-size:21px;color:var(--wine);text-align:center;line-height:36px}

/* left column */
.locations{left:136px;top:740px;width:261px;height:330px;background:var(--plum);border-radius:0 26px 26px 26px;padding:38px 14px 0 14px;color:var(--white)}
.services{left:136px;top:448px;width:261px;height:312px;background:var(--magenta);border-radius:26px 26px 26px 0;padding:12px 14px 0}
.panel-title{font-family:"Quicksand",sans-serif;font-weight:500;font-size:32px;color:var(--white);text-align:center;padding-bottom:6px;border-bottom:1px solid rgba(255,255,255,.8)}
.service-list{list-style:none;margin:16px 0 0 24px}
.service-list li{font-family:"Quicksand",sans-serif;font-weight:500;font-size:17px;color:var(--white);height:36.4px;position:relative;padding-left:12px}
.service-list li::before{content:"";position:absolute;left:0;top:7px;width:7px;height:7px;border-radius:50%;background:#f0b0d4}
.read-more{position:absolute;right:14px;bottom:12px;font-size:12px;color:var(--white)}
.office{font-family:"Quicksand",sans-serif;font-size:15px;line-height:15.5px;margin-top:12px}
.office.pink{color:#f2a6d0}
.office dl{display:grid;grid-template-columns:44px 1fr;margin-top:8px;color:var(--white)}
.office + .office{margin-top:30px}
.see-map{position:absolute;right:14px;bottom:10px;font-size:12px}

/* content */
.diagnostic{left:413px;top:815px;width:503px;height:255px;background:var(--sky-deep);border-radius:26px 0 26px 26px;padding:20px 15px 0}
.welcome-box{left:413px;top:447px;width:503px;height:382px;background:var(--white);border-radius:26px 26px 26px 0}
.welcome-title{left:428px;top:448px;font-family:"Parisienne",cursive;font-size:46px;color:var(--plum-text)}
.copy{font-size:12px;line-height:13.4px}
.welcome-text{left:431px;top:516px;width:232px;color:#333}
.goal-text{left:429px;top:663px;width:234px;color:var(--plum-text)}
.preg-title{left:675px;top:458px;width:208px;text-align:center;font-family:"Quicksand",sans-serif;font-size:25px;color:#8a949c;border-bottom:1px solid #c7cdd2;padding-bottom:4px}
.photo-exam{left:672px;top:505px;width:226px;height:145px;background:linear-gradient(#b9c3cc,#8a9aa6)}
.preg-text{left:672px;top:663px;width:226px;color:var(--grey-text)}
.btn-more{width:82px;height:28px;border-radius:14px;font-family:"Quicksand",sans-serif;font-weight:700;font-size:19px;color:var(--white);text-align:center;line-height:28px}
.btn-more.pink{background:var(--magenta)}
.btn-more.blue{background:var(--sky-deep)}
.diag-title{font-family:"Quicksand",sans-serif;font-weight:700;font-size:25px;color:var(--white);padding-bottom:4px;border-bottom:1px solid rgba(255,255,255,.7)}
.diag-text{color:var(--white);margin-top:16px;letter-spacing:-.1px}
.photo-visit{left:431px;top:950px;width:119px;height:81px;background:linear-gradient(90deg,#d9cabd,#eef0f2)}
.visit-text{left:560px;top:956px;width:330px;color:var(--plum)}

/* footer */
.footer{left:0;top:1083px;width:1040px;height:96px;background:var(--footer)}
.footer-col{top:1090px;font-size:13px;line-height:16.7px;color:var(--footer-text)}
.footer-col h4{font-size:13px;color:var(--footer-head);font-weight:700}
.copyright{left:0;top:1179px;width:1040px;height:21px;background:var(--magenta);color:#f2b8da;font-size:12.5px;font-weight:700;text-align:center;line-height:21px}
</style>
</head>
<body>

<div class="abs hero"></div>
<div class="abs silhouette" role="img" aria-label="Soft silhouette of an expectant mother"></div>
<div class="abs navbar"></div>
<ul class="abs nav">
  <li class="active">HOME</li>
  <li>PATIENT INFORMATION</li>
  <li>HEALTH</li>
  <li>PREGNANCY</li>
  <li>MEDIA</li>
  <li>LOCATIONS</li>
</ul>
<div class="abs brand">
  <div class="brand-name">Dr. Hart</div>
  <div class="brand-tag">OBSTETRICS &amp; GYNECOLOGY</div>
</div>

<div class="abs portrait" role="img" aria-label="Portrait of Dr. Lin-Yue Hart in a white coat"></div>

<div class="abs call"><small>Call for Appointment</small><strong>(555) 214-3360</strong></div>
<div class="abs hero-title"><b>Serving</b><span>all areas of women's health</span></div>
<p class="abs hero-lead">Lorem ipsum dolor sit amet, consectetur adipisicing elit, sed do eiusmod tempor incididunt ut labore et dolore magna aliqua. Ut enim ad minim veniam, quis nostrud ...</p>
<div class="abs btn-learn">Learn More</div>

<section class="abs locations">
  <h2 class="panel-title">Locations</h2>
  <div class="office">
    2240 Harbor Crest Avenue<br>Suite 115-116<br>Westvale, Florida&nbsp; 33400
    <dl><dt>Tel:</dt><dd>(555) 214-3360</dd><dt>Fax:</dt><dd>(555) 214-3361</dd></dl>
  </div>
  <div class="office pink">
    780 N.W. 9th Street<br>Suite 110A<br>Palmer, Florida&nbsp; 33410
    <dl><dt>Tel:</dt><dd>(555) 308-7720</dd><dt>Fax:</dt><dd>(555) 308-7721</dd></dl>
  </div>
  <span class="see-map">see the map...</span>
</section>

<section class="abs services">
  <h2 class="panel-title">Our services</h2>
  <ul class="service-list">
    <li>Obstetrics</li>
    <li>Family Planning</li>
    <li>Hormonal Evaluation</li>
    <li>Incontinence</li>
    <li>Infertility</li>
    <li>Gynecology Surgery</li>
  </ul>
  <span class="read-more">read more...</span>
</section>

<section class="abs diagnostic">
  <h2 class="diag-title">Diagnostic Tests Performed</h2>
  <p class="copy diag-text">Sed ut perspiciatis unde omnis iste natus error sit voluptatem accusantium doloremque laudantium, totam rem aperiam, eaque ipsa quae ab illo inventore veritatis et quasi architecto beatae vitae dicta sunt explicabo. Nemo enim ipsam voluptatem quia voluptas sit aspernatur aut odit aut fugit,</p>
</section>
<div class="abs photo-visit" role="img" aria-label="Dr. Hart talking with a patient"></div>
<p class="abs copy visit-text">Ut enim ad minim veniam, quis nostrud exercitation ullamco laboris nisi ut aliquip ex ea commodo consequat. Duis aute irure dolor in reprehenderit in voluptate velit esse cillum dolore eu fugiat nulla pariatur...</p>
<div class="abs btn-more pink" style="left:816px;top:1030px">More</div>

<section class="abs welcome-box"></section>
<h2 class="abs welcome-title">Welcome</h2>
<p class="abs copy welcome-text">Welcome to Dr. Lin-Yue Hart's website. Here you will be able to find information about both of our offices, meet Dr. Hart and her staff, and browse through our women's health links to learn more about pregnancy, nutrition, exercise, and other women's health issues. Have fun and if you have any questions, feel free to contact us at office@harthealthmail.net</p>
<p class="abs copy goal-text">Dr. Hart's goal is to provide current and compassionate women's healthcare in a fashion that acknowledges her patients' diverse values, backgrounds, and conditions. Dr. Hart acknowledges the whole individual and recognizes the inseparability of the body, mind, and spirit...</p>
<h3 class="abs preg-title">The Pregnancy</h3>
<div class="abs photo-exam" role="img" aria-label="Examination room with ultrasound equipment"></div>
<p class="abs copy preg-text">Lorem ipsum dolor sit amet, consectetur adipisicing elit, sed do eiusmod tempor incididunt ut labore et dolore magna aliqua. Ut enim ad minim veniam, quis nostrud exercitation ullamco laboris nisi ut aliquip ex ea commodo consequat. Duis aute irure dolor in reprehenderit in...</p>
<div class="abs btn-more pink" style="left:575px;top:791px">More</div>
<div class="abs btn-more blue" style="left:816px;top:790px">More</div>

<footer>
  <div class="abs footer"></div>
  <div class="abs footer-col" style="left:137px"><h4>About Us</h4>History<br>Our Staff<br>Dr. Hart</div>
  <div class="abs footer-col" style="left:263px"><h4>Patient Information</h4>Appointments<br>E-Prescriptions<br>Payments Accepted<br>Insurance</div>
  <div class="abs footer-col" style="left:427px"><h4>Health</h4>General<br>Sexual,<br>Mental<br>Affiliates</div>
  <div class="abs footer-col" style="left:542px"><h4>Pregnancy</h4>Minimally invasive surgery<br>4-D Ultra Sound<br>Hospital Affiliations</div>
  <div class="abs footer-col" style="left:729px"><h4>Media</h4>News<br>Pictures<br>Videos</div>
  <div class="abs footer-col" style="left:827px"><h4>Locations</h4>Palmer Office,<br>Westvale Office</div>
  <div class="abs copyright">Copyright © 2011 Lin-Yue Hart, M.D., P.A.</div>
</footer>

</body>
</html>
```